The Horizonfold LLC Asset Classes

I'm looking for for two designs here to go into powerpoint and potentially as a standalone PDF. My company does wealth management.
Graphic Image #1
I break down the investment world into 4 broad categories
-Preservation
-Capital Markets
-Real Estate
-Alternatives
In each broad category, there are subcategories:
Preservation: cash, checking/savings accounts, money market accounts, CD's, and fixed annuities.
Capital Markets: Publicly traded stocks and bonds
Real Estate: single-family residence, retail, industrial, multifamily, and office
Alternatives: private equity, private credit, cryptocurrency, asset-backed loans, tax liens, oil & gas, litigation finance, and royalties
Graphic 2: Please see the bottom f page 1 of the Lanternway Briefings PDF.
Just like in graphic one, you have 4 categories of the Capital Markets and their respective subcategories
Category 1: Domestic Stocks: Subcategories are Large, mid, and small size companies
Category 2: International Stocks: Subcategories are Large, Mid/Small and by region - Developed and Emerging
Category 3: Fixed Income: You have subcategories like corporate, municipal, government, domestic, international
Category 4: Alternatives: The subcategories are metals and real estate
---------------------
I'm looking to create a graphic (either pie chart, or a circle broken into parts or some other clever way to illustrate this) to clearly illustrate both of these universes in a clean, professional, slick manner.
Target Market(s)
Investors
Colors
Designer to choose colors to be used in the design.
Requirements
Must have
- Clean
- professional
- Easy to read
- Creative
- Visually appealling
Nice to have
- I have attached my logo and some marketing materials so you can get a feel of what I am doing. Maybe you can clean this up too!

```html
<!DOCTYPE html>
<html lang="en">
<head>
<meta charset="utf-8">
<title>The Horizonfold LLC – Capital Markets Asset Classes</title>
<link href="https://fonts.googleapis.com/css2?family=Oswald:wght@300;400;500&display=swap" rel="stylesheet">
<style>
  :root {
    --domestic: #6b8fae;
    --international: #f59a28;
    --fixed: #1a9c9a;
    --alternatives: #9b9a7b;
    --brand-navy: #1e5a8c;
    --brand-orange: #f0962c;
    --wave-start: #17507f;
    --wave-end: #2fa9b9;
    --paper: #ffffff;
  }
  * { margin: 0; padding: 0; box-sizing: border-box; }
  html, body { width: 1200px; height: 843px; overflow: hidden; background: var(--paper); }
  .board {
    position: relative;
    width: 1200px;
    height: 843px;
    font-family: "Oswald", "Arial Narrow", sans-serif;
    color: var(--paper);
  }
  .shapes { position: absolute; inset: 0; }
  .category-title {
    position: absolute;
    top: 22px;
    height: 131px;
    display: flex;
    align-items: center;
    justify-content: center;
    text-align: center;
    font-weight: 300;
    font-size: 35px;
    line-height: 1.45;
  }
  .tile {
    position: absolute;
    width: 266px;
    height: 83px;
    display: flex;
    align-items: center;
    justify-content: center;
    font-weight: 500;
    font-size: 27px;
    white-space: nowrap;
  }
  .tile--light { font-weight: 300; }
  .tile--domestic { background: var(--domestic); }
  .tile--international { background: var(--international); }
  .tile--fixed { background: var(--fixed); }
  .tile--alternatives { background: var(--alternatives); }
  .col-1 { left: 30px; }
  .col-2 { left: 314px; }
  .col-3 { left: 598px; }
  .col-4 { left: 882px; }
  .row-1 { top: 171px; }
  .row-2 { top: 266px; }
  .row-3 { top: 360px; }
  .row-4 { top: 454px; }
  .row-5 { top: 550px; }
  .brand {
    position: absolute;
    left: 24px;
    top: 672px;
    display: flex;
    align-items: center;
    gap: 12px;
  }
  .brand-dot {
    width: 34px;
    height: 34px;
    border-radius: 50%;
    background: var(--brand-orange);
  }
  .brand-name {
    font-family: "Oswald", "Arial Narrow", sans-serif;
    font-weight: 500;
    font-size: 32px;
    color: var(--brand-navy);
  }
</style>
</head>
<body>
<main class="board">
  <svg class="shapes" width="1200" height="843" viewBox="0 0 1200 843" aria-hidden="true">
    <defs>
      <linearGradient id="wave-fill" x1="0" y1="0" x2="1" y2="0">
        <stop offset="0" stop-color="var(--wave-start)"/>
        <stop offset="0.6" stop-color="#1f7399"/>
        <stop offset="1" stop-color="var(--wave-end)"/>
      </linearGradient>
    </defs>
    <g stroke="var(--paper)" stroke-width="2">
      <polygon fill="var(--alternatives)" points="878,22 1160,22 1182,87 1160,153 878,153 900,87"/>
      <polygon fill="var(--fixed)" points="594,22 878,22 900,87 878,153 594,153 616,87"/>
      <polygon fill="var(--international)" points="310,22 594,22 616,87 594,153 310,153 333,87"/>
      <polygon fill="var(--domestic)" points="27,22 310,22 333,87 310,153 27,153 49,87"/>
    </g>
    <path class="wave" fill="url(#wave-fill)"
      d="M0,843 L0,790 C70,762 300,762 600,782 C850,798 1050,780 1200,744 L1200,843 Z"/>
  </svg>

  <h2 class="category-title" style="left:49px;width:270px;">Domestic<br>Stocks</h2>
  <h2 class="category-title" style="left:333px;width:270px;">International<br>Stocks</h2>
  <h2 class="category-title" style="left:616px;width:270px;">Fixed Income</h2>
  <h2 class="category-title" style="left:900px;width:270px;">Alternatives</h2>

  <div class="tile tile--domestic col-1 row-1">Large size companies</div>
  <div class="tile tile--domestic col-1 row-2">Mid size companies</div>
  <div class="tile tile--domestic col-1 row-3">Small size companies</div>

  <div class="tile tile--international col-2 row-1">Large</div>
  <div class="tile tile--international col-2 row-2">Mid</div>
  <div class="tile tile--international col-2 row-3">Small</div>
  <div class="tile tile--international tile--light col-2 row-4">Developed regions</div>
  <div class="tile tile--international tile--light col-2 row-5">Emerging regions</div>

  <div class="tile tile--fixed col-3 row-1">Corporate</div>
  <div class="tile tile--fixed col-3 row-2">Municipal</div>
  <div class="tile tile--fixed col-3 row-3">Government</div>
  <div class="tile tile--fixed col-3 row-4">Domestic</div>
  <div class="tile tile--fixed col-3 row-5">International</div>

  <div class="tile tile--alternatives col-4 row-1">Metals</div>
  <div class="tile tile--alternatives col-4 row-2">Estate</div>

  <div class="brand">
    <span class="brand-dot"></span>
    <span class="brand-name">The Horizonfold LLC</span>
  </div>
</main>
</body>
</html>
```